Unique and original Business Card for Financial Services Business

I have moved premises and need to change the detail on my business card so thought now is a good time for a re-design. Looking for something professional and modern with colours to fit in with out logo. Like the idea of foil or embossing if that works but not a must have but I do want something that stands out and that I could not design myself.

Once business card is designed I will also be looking to get letterhead and flyers done but want the business card concept in place first.

The majority of designs I am receiving are generic and template based. I am looking for something unique and original. We have some great design elements in our logo, think outside the box and show me something that stands out from the crowd.

Target Market(s)

Business Professionals

Industry/Entity Type

Finance

Contact Information for Business Card

Name: Delia Norwood Phone 0473 958 162 Address PO Box 8617 Mossvale NSW 2389 Email info@steadyharbourfinancialservices.com.au website www.steadyharbourfinancialservices.com.au

Font styles to use
Other font styles liked:
• Ralway

Requirements
Should not have
• No black backgrounds please

```html
<!DOCTYPE html>
<html lang="en">
<head>
<meta charset="utf-8">
<title>Steady Harbour Financial Services – Business Card</title>
<link rel="stylesheet" href="https://fonts.googleapis.com/css2?family=Raleway:wght@400;500&display=swap">
<style>
  :root {
    --teal: #0f7d86;
    --charcoal: #3c3c3c;
    --ink: #454545;
    --paper: #ffffff;
    --edge: #cfcfcf;
    --bar-text: #f2f2f2;
  }
  html, body {
    margin: 0;
    width: 1200px;
    height: 1200px;
    overflow: hidden;
    background: var(--paper);
    font-family: "Raleway", sans-serif;
  }
  .card {
    position: absolute;
    left: 75px;
    top: 300px;
    width: 1051px;
    height: 600px;
    background: var(--paper);
    border: 1px solid var(--edge);
    box-sizing: border-box;
    overflow: hidden;
  }
  .accent-rule {
    position: absolute;
    left: 0;
    top: 58px;
    width: 765px;
    height: 4px;
    background: var(--teal);
  }
  .accent-tab {
    position: absolute;
    left: 88px;
    top: 58px;
    width: 170px;
    height: 28px;
    background: var(--teal);
    border-radius: 0 0 13px 13px;
  }
  .brand {
    position: absolute;
    right: 84px;
    top: 58px;
    display: flex;
    align-items: center;
    gap: 16px;
  }
  .brand-mark {
    width: 56px;
    height: 56px;
    flex: none;
    background: var(--teal);
  }
  .brand-name {
    margin: 0;
    font-size: 30px;
    font-weight: 400;
    line-height: 1.15;
    color: var(--teal);
  }
  .person {
    position: absolute;
    left: 85px;
    top: 112px;
  }
  .person-name {
    margin: 0;
    font-size: 52px;
    font-weight: 500;
    color: var(--charcoal);
    line-height: 1.05;
  }
  .person-title {
    margin: 0;
    font-size: 34px;
    font-weight: 400;
    color: var(--teal);
    line-height: 1.1;
  }
  .address {
    position: absolute;
    left: 85px;
    top: 232px;
    margin: 0;
    font-style: normal;
    font-size: 25px;
    line-height: 31px;
    color: var(--ink);
  }
  .contact-list {
    position: absolute;
    left: 85px;
    top: 372px;
    margin: 0;
    padding: 0;
    list-style: none;
    font-size: 25px;
    color: var(--ink);
  }
  .contact-item {
    display: flex;
    align-items: center;
    height: 34px;
    margin-bottom: 8px;
  }
  .contact-icon {
    width: 26px;
    height: 26px;
    margin-right: 10px;
    fill: var(--teal);
  }
  .web-bar {
    position: absolute;
    left: 90px;
    right: 0;
    top: 498px;
    height: 48px;
    background: var(--charcoal);
    display: flex;
    align-items: center;
    padding-left: 42px;
    font-size: 26px;
    color: var(--bar-text);
  }
  .web-emblem {
    position: absolute;
    left: 82px;
    top: 494px;
    width: 30px;
    height: 44px;
    background: var(--teal);
    border-radius: 40%;
  }
</style>
</head>
<body>
  <main class="card">
    <div class="accent-rule"></div>
    <div class="accent-tab"></div>

    <div class="brand">
      <span class="brand-mark" role="img" aria-label="Company logo mark"></span>
      <p class="brand-name">Steady Harbour<br>Financial Services</p>
    </div>

    <header class="person">
      <h1 class="person-name">Delia Norwood</h1>
      <p class="person-title">President</p>
    </header>

    <address class="address">
      PO Box 8617<br>
      Mossvale<br>
      NSW 2389
    </address>

    <ul class="contact-list">
      <li class="contact-item">
        <svg class="contact-icon" viewBox="0 0 24 24" aria-hidden="true">
          <path d="M6.6 10.8c1.4 2.8 3.8 5.1 6.6 6.6l2.2-2.2c.3-.3.7-.4 1-.2 1.1.4 2.3.6 3.6.6.6 0 1 .4 1 1V20c0 .6-.4 1-1 1C10.6 21 3 13.4 3 4c0-.6.4-1 1-1h3.5c.6 0 1 .4 1 1 0 1.3.2 2.5.6 3.6.1.3 0 .7-.2 1L6.6 10.8z"/>
        </svg>
        <span>0473 958 162</span>
      </li>
      <li class="contact-item">
        <svg class="contact-icon" viewBox="0 0 24 24" aria-hidden="true">
          <path d="M2 5h20v14H2z M3.5 6.5v.4l8.5 6 8.5-6v-.4z M3.5 8.7v8.8l5.6-4.9z M20.5 8.7l-5.6 3.9 5.6 4.9z M10.3 13.4l-5.6 4.6h14.6l-5.6-4.6-1.7 1.2z" fill-rule="evenodd"/>
        </svg>
        <span>info@steadyharbourfinancialservices.com.au</span>
      </li>
    </ul>

    <div class="web-bar">www.steadyharbourfinancialservices.com.au</div>
    <div class="web-emblem" role="img" aria-label="Small bird emblem"></div>
  </main>
</body>
</html>
```